PREMIUM AGENCY High End Business Card - A+++ Designers Wanted

** DO NOT ATTEMPT TO CONTACT ME THROUGH SEARCHING ON ZINTREL OR EMAILING ME THROUGH MY WEBSITE **

I need a fresh, contemporary business card designed using the logo attached (BRONSALK)

I have attached the font for BRONSALK

It must have a premium look and feel. The business card size must be STANDARD size.

You can submit either/both VERTICAL or HORIZONTAL designs.

FRONT: It must have the following sample information on

Paul Ardley
Director Operations
Mobile +61 452 118 906
Email paulardley@bronsalk.com
www.bronsalk.com

The REAR of the business card must have the words

CREATE INSPIRE TOMORROW

as part of the design, in the same font (NEXA) attached.

The words do not need to be in capitals, or on the same line, please design this as you see it best working.

ADDITIONAL INFORMATION
======================

The BRONSALK logo must be on the front of the card

I want Ultraviolet printing on the final design, to enhance either the NAME of the person OR the BRONSALK logo OR the words on the back of the card.

Target Market(s)

Agency, Advertising Agency, Creative, Designers

Industry/Entity Type

Media

Contact Information for Business Card

Design Agency, Contemporary, Premium look and feel, High Quality

Font styles to use
Serif
Sans Serif
Other font styles liked:
• ATTACHED TO PROJECT

Requirements
Must have
• BLACK & WHITE as the primary design, and if you feel there can be a highlighted colour, then this can be used.
• The Logo ICON attached is blue, this colour must not be changed.
• I have attached the partner brand BRONSALK MEDIA incase you need to manipulate the original files.
• ** DO NOT ATTEMPT TO CONTACT ME THROUGH SEARCHING ON ZINTREL OR EMAILING ME THROUGH MY WEBSITE **
Nice to have
• Must be Premium. I have attached some sample designs, that I like that would be a good inspiration for where this can be taken.
• My favourite design is is the KESTRAVUE2-BUSINESSCARD-TEMPLATE
Should not have
• No funny or silly standard / off the shelf designs

```html
<!DOCTYPE html>
<html lang="en">
<head>
<meta charset="utf-8">
<title>Bronsalk Business Card</title>
<link rel="stylesheet" href="https://fonts.googleapis.com/css2?family=Lato:wght@400;700;900&display=swap">
<style>
  :root {
    --page-bg: #2b2d30;
    --card-back: #47535a;
    --card-front: #5b6b73;
    --card-front-shade: #4d5b62;
    --brand-blue: #2a9fe0;
    --stripe-blue: #1a96de;
    --text-light: #ffffff;
    --text-soft: #e6ecef;
    --rule: #c9d2d6;
  }
  * { box-sizing: border-box; margin: 0; padding: 0; }
  html, body {
    width: 1200px;
    height: 900px;
    overflow: hidden;
    background: var(--page-bg);
    font-family: "Lato", sans-serif;
  }
  .sheet {
    width: 1200px;
    height: 900px;
    display: flex;
    flex-direction: column;
    align-items: center;
    justify-content: center;
    gap: 44px;
  }
  .card {
    position: relative;
    width: 700px;
    height: 400px;
    overflow: hidden;
    box-shadow: 0 14px 30px rgba(0,0,0,0.45);
  }

  /* Back of card */
  .card--back { background: var(--card-back); }
  .back-brand {
    position: absolute;
    left: 0; right: 0;
    top: 118px;
    display: flex;
    align-items: center;
    justify-content: center;
    gap: 16px;
  }
  .back-brand__dot {
    width: 34px; height: 34px;
    border-radius: 50%;
    background: var(--brand-blue);
  }
  .back-brand__name {
    font-weight: 900;
    font-size: 44px;
    letter-spacing: 6px;
    color: var(--brand-blue);
  }
  .tagline {
    position: absolute;
    left: 0; right: 0;
    top: 238px;
    text-align: center;
    font-weight: 400;
    font-size: 27px;
    letter-spacing: 4px;
    color: var(--text-light);
  }

  /* Front of card */
  .card--front { background: var(--card-front); }
  .front-watermark {
    position: absolute;
    right: -90px;
    bottom: -120px;
    width: 380px;
    height: 380px;
    border-radius: 50%;
    background: var(--card-front-shade);
  }
  .front-stripe {
    position: absolute;
    left: 0; right: 0; bottom: 0;
    height: 12px;
    background: var(--stripe-blue);
  }
  .front-brand {
    position: absolute;
    left: 48px;
    top: 46px;
    display: flex;
    align-items: center;
    gap: 18px;
  }
  .front-brand__dot {
    width: 40px; height: 40px;
    border-radius: 50%;
    background: var(--brand-blue);
  }
  .front-brand__name {
    font-weight: 900;
    font-size: 54px;
    letter-spacing: 9px;
    color: var(--text-light);
  }
  .contact {
    position: absolute;
    left: 66px;
    top: 168px;
    padding-left: 28px;
    border-left: 1.5px solid var(--rule);
    padding-top: 6px;
    padding-bottom: 6px;
  }
  .contact__name {
    font-size: 28px;
    font-weight: 400;
    color: var(--brand-blue);
    line-height: 1.1;
  }
  .contact__role {
    font-size: 19px;
    color: var(--text-soft);
    margin-bottom: 16px;
  }
  .contact__list { list-style: none; }
  .contact__item {
    display: flex;
    align-items: center;
    gap: 12px;
    font-size: 19px;
    color: var(--text-light);
    line-height: 1.5;
  }
  .contact__icon {
    width: 16px; height: 16px;
    flex: none;
  }
</style>
</head>
<body>
<main class="sheet">

  <section class="card card--back" aria-label="Card back">
    <div class="back-brand">
      <span class="back-brand__dot"></span>
      <span class="back-brand__name">BRONSALK</span>
    </div>
    <p class="tagline">CREATE INSPIRE TOMORROW</p>
  </section>

  <section class="card card--front" aria-label="Card front">
    <div class="front-watermark"></div>
    <div class="front-brand">
      <span class="front-brand__dot"></span>
      <span class="front-brand__name">BRONSALK</span>
    </div>
    <div class="contact">
      <p class="contact__name">Paul Ardley</p>
      <p class="contact__role">Director Operations</p>
      <ul class="contact__list">
        <li class="contact__item">
          <svg class="contact__icon" viewBox="0 0 16 16" aria-hidden="true">
            <rect x="4" y="1" width="8" height="14" rx="1.5" fill="none" stroke="#2a9fe0" stroke-width="1.6"/>
            <rect x="6" y="12" width="4" height="1.2" fill="#2a9fe0"/>
          </svg>
          +61 452 118 906
        </li>
        <li class="contact__item">
          <svg class="contact__icon" viewBox="0 0 16 16" aria-hidden="true">
            <rect x="1" y="3" width="14" height="10" fill="#2a9fe0"/>
            <path d="M1 3 L8 9 L15 3" fill="none" stroke="#5b6b73" stroke-width="1.4"/>
          </svg>
          paulardley@bronsalk.com
        </li>
        <li class="contact__item">
          <svg class="contact__icon" viewBox="0 0 16 16" aria-hidden="true">
            <circle cx="8" cy="8" r="6.5" fill="#2a9fe0"/>
            <path d="M1.5 8 H14.5 M8 1.5 V14.5" stroke="#5b6b73" stroke-width="1"/>
            <ellipse cx="8" cy="8" rx="3" ry="6.5" fill="none" stroke="#5b6b73" stroke-width="1"/>
          </svg>
          www.bronsalk.com
        </li>
      </ul>
    </div>
    <div class="front-stripe"></div>
  </section>

</main>
</body>
</html>
```